Women's Empowerment & Prayer Brunch - Matching Poster, flyer and Postcard

We are a Christian Event & Travel Company and we are hosting our inaugural event on June 10, 2017. This event is a women's empowerment & prayer brunch aboard a private yacht leaving out of Larkspur Landing, Maryland. The event will cater to women who have a vision to start or have already embarked on the journey of starting or growing a business or ministry. The event calls for a matching poster, flyer and postcard design that give an elegant & exquisite feel with just the right breath of freshness. The colors should reflect our logo as this is our launch event. I have also included 2 photos of the Coralwind Heritage Village production (one of our sponsors) - Please include but do not make it take over the design - this is to advertise the door prize. The final design will portray the branding of the company (Christian, travel, events, elegance, professional), the branding of the event (elegant and luxurious) and the importance of this launch event.
Please include the following information:
Brightwell Event & Travel Group presents
Event name: Climbing the Hill: Trust, Service & Devotion.
Tag Line/Description: An Exquisite Women's Empowerment & Prayer Brunch.
Guest Speaker: Minister Harriet L. Dunmore (Photo included)
VP of TrustLine
Asst. Pastor & First Lady of Gilead Baptist Church
Special Guest Psalmist: Minister Tessa Holbrook (Photo Included)
Worship Director of Stonefield Community Church
Vocalist, Songwriter, Musician, and Clinician
Venue: Aboard the Regal Tide Yacht
Dock: Larkspur Landing
342 Marlow Court, Oxen Hill, MD 20712
Boarding 10:00am
Sailing Promptly at 10:30am
(Please be on time the yacht will not wait)
Date: Saturday June 10, 2017
Tickets: Early Bird US$75.00/person (ends May 15, 2017)
Regular Tickets US$95.99
Purchase Tickets at www.brightwellevent-travel.example/climbing-the-hill
SPACE IS LIMITED DUE TO YACHT CAPACITY
Grand Prize: Julian Ardent Purse
Door Prize: 2 Tickets to the Islander Coralwind Heritage Village
Other prizes for special ladies in attendance.
Ladies are asked to dress in Elegant White Ensemble
Corporate Sponsors:
The Coralwind Heritage Village (Logo included)
R. Lanning Photography (Logo included)
Special Thanks to our Individual Sponsors:
Mrs. G. Whitlow, Mr. K Prentice & Mr. S. Dorsey

Target Market(s)

Women, Business, Ministry, Christians, Middle to Upper Class

Industry/Entity Type

Events

Font styles to use
Serif
Script

Requirements
Must have
• Elegance, professional, vivid in color & font. be creative in Visual and FONT!
• Poster: 18" X 24"
• Flyer: one sided.
• ***** the final design chosen will have a cross referenced design of 1 flyer, 1 postcard 1 poster. This was included so you have a reference - Be creative!!!!!!
Nice to have
• Matching across all 3 designs (poster, flyer & postcard) but sized appropriately and just enough difference to play up the design and be appealing.
• I uploaded 3 example flyers to give you inspiration of the type of visuals I'm looking for. I removed my amateur sample because the designs were copying it instead of being creative.
Should not have
• Any thing inappropriate, alcohol oriented or sexual

```html
<!DOCTYPE html>
<html lang="en">
<head>
<meta charset="utf-8">
<title>Climbing the Hill – Women's Empowerment &amp; Prayer Brunch</title>
<link rel="stylesheet" href="https://fonts.googleapis.com/css2?family=Playfair+Display:wght@700;900&family=Great+Vibes&family=Dancing+Script:wght@600;700&family=Arimo:wght@400;700&family=Libre+Baskerville:wght@700&display=swap">
<style>
:root{
  --navy:#1b2c8f;
  --royal:#1f32d6;
  --magenta:#e0369c;
  --maroon:#5b1212;
  --wine:#7d1616;
  --gold:#c9a43a;
  --ink:#2a1a10;
}
*{margin:0;padding:0;box-sizing:border-box}
html,body{width:900px;height:1200px;overflow:hidden}
body{background:#fff}
.poster{
  position:relative;width:900px;height:1200px;overflow:hidden;
  background:
    radial-gradient(ellipse 260px 200px at 470px 420px, rgba(255,255,240,.95), rgba(255,255,240,0) 70%),
    radial-gradient(ellipse 240px 170px at 760px 300px, rgba(60,110,170,.55), rgba(60,110,170,0) 75%),
    radial-gradient(ellipse 300px 200px at 120px 120px, rgba(120,200,225,.55), rgba(120,200,225,0) 75%),
    linear-gradient(180deg,#bfe7f1 0%,#dff3f0 28%,#eef6e6 48%,#f7efc2 66%,#f6d16a 84%,#f2ae3c 100%);
  font-family:"Arimo",Arial,sans-serif;
}
.brand-mark{
  position:absolute;left:400px;top:0;width:100px;height:86px;background:var(--navy);
  display:flex;align-items:center;justify-content:center;text-align:center;padding:6px;
}
.brand-mark span{color:var(--gold);font-family:"Playfair Display",serif;font-weight:700;font-size:11px;line-height:1.2}
.presents{position:absolute;top:88px;left:0;width:900px;text-align:center;font-weight:700;font-size:13px;color:var(--navy);letter-spacing:.5px}
.title{position:absolute;top:98px;left:0;width:900px;text-align:center;font-family:"Playfair Display",serif;font-weight:900;font-size:60px;color:var(--royal);line-height:1}
.subtitle{position:absolute;top:158px;right:140px;font-family:"Playfair Display",serif;font-weight:700;font-size:15px;line-height:18px;color:var(--navy)}
.tagline{position:absolute;top:182px;left:0;width:900px;text-align:center;font-family:"Great Vibes",cursive;font-size:39px;word-spacing:6px;color:var(--magenta);line-height:1.1;white-space:nowrap}

.portrait{position:absolute;border-radius:50%}
.portrait.speaker{left:34px;top:236px;width:208px;height:208px;background:radial-gradient(circle at 50% 45%,#b5715a 0%,#c2281f 55%,#7a2a1f 100%)}
.portrait.psalmist{left:36px;top:566px;width:206px;height:206px;background:radial-gradient(circle at 50% 50%,#a06a4e 0%,#4a3328 50%,#111 100%)}
.caption{position:absolute;text-align:center;font-weight:700}
.caption.speaker{left:18px;top:466px;width:240px;font-size:13.5px;line-height:17px;color:var(--wine)}
.caption.psalmist{left:18px;top:788px;width:240px;font-size:12.5px;line-height:16px;color:var(--maroon)}

.venue{position:absolute;left:364px;top:0;width:460px;height:460px;text-align:center;color:var(--royal)}
.venue div{position:absolute;left:0;width:100%;white-space:nowrap}
.venue .aboard{top:240px;font-family:"Libre Baskerville",serif;font-weight:700;font-size:28px}
.venue .yacht{top:280px;font-size:37px}
.venue .dock{top:322px;font-size:29px}
.venue .address{top:362px;font-weight:700;font-size:15.5px}
.venue .boarding{top:390px;font-weight:700;font-size:16.5px}
.venue .sailing{top:412px;font-weight:700;font-size:16.5px}
.venue .on-time{top:435px;font-weight:700;font-size:12px;color:var(--maroon)}

.date-pill{
  position:absolute;left:387px;top:458px;width:329px;height:52px;border-radius:26px;
  background:linear-gradient(180deg,#6e1b1b,var(--maroon));box-shadow:0 4px 6px rgba(0,0,0,.25);
  display:flex;align-items:center;justify-content:center;
  color:#fff;font-family:"Dancing Script",cursive;font-weight:700;font-size:29px;
}
.tickets{position:absolute;left:360px;top:524px;width:340px;text-align:center;color:var(--royal);font-weight:700;font-size:14.5px;line-height:19px}
.purchase{position:absolute;left:230px;top:588px;width:660px;text-align:center;color:var(--royal);font-weight:700;font-size:18.5px;line-height:23px;white-space:nowrap}
.capacity{position:absolute;left:230px;top:638px;width:660px;text-align:center;color:var(--maroon);font-weight:700;font-size:12.5px;letter-spacing:1px}

.prize-ribbon{position:absolute;left:330px;top:664px;width:436px;height:212px}
.prize-text{position:absolute;left:350px;top:764px;width:396px;text-align:center;color:#fff;font-family:"Libre Baskerville",serif;font-weight:700}
.prize-text .grand{font-size:17.5px;margin-bottom:9px}
.prize-text .door{font-size:14.5px;line-height:19px}
.prize-text .other{font-size:11.5px;line-height:16px;margin-top:6px;color:#f3dfa6}

.dress-code{position:absolute;left:237px;top:886px;width:640px;text-align:center;font-family:"Dancing Script",cursive;font-weight:600;font-size:25px;line-height:30px;color:var(--royal);white-space:nowrap}
.sponsor-bar{
  position:absolute;z-index:2;left:282px;top:933px;width:322px;height:24px;
  background:linear-gradient(90deg,rgba(201,164,58,.1),#b8902e 25%,#8d6a20 50%,#b8902e 75%,rgba(201,164,58,.1));
  text-align:center;font-family:"Libre Baskerville",serif;font-weight:700;font-size:15px;line-height:24px;color:#fff;
}
.scene{position:absolute;top:979px;width:224px;height:149px}
.scene.dance{left:34px;background:radial-gradient(ellipse at 50% 70%,#d9a94a 0%,#6a3a1c 40%,#1a0f08 85%)}
.scene.fire{left:639px;background:radial-gradient(ellipse at 50% 55%,#f08a2a 0%,#7a2c10 35%,#0b0604 75%)}
.sponsor-badge{
  position:absolute;top:946px;width:180px;height:180px;border-radius:50%;
  border:10px solid var(--gold);background:#fff;
  display:flex;align-items:center;justify-content:center;text-align:center;padding:20px;
  font-family:"Libre Baskerville",serif;font-weight:700;font-size:14px;line-height:19px;color:#8a6a1f;
}
.sponsor-badge.heritage{left:268px}
.sponsor-badge.lanning{left:452px;color:#555}
.thanks{position:absolute;left:0;top:1138px;width:900px;text-align:center;font-family:"Libre Baskerville",serif;font-weight:700;font-size:14px;line-height:21px;color:var(--ink)}
</style>
</head>
<body>
<main class="poster">
  <div class="brand-mark"><span>Brightwell Event &amp; Travel Group</span></div>
  <div class="presents">PRESENTS</div>
  <h1 class="title">Climbing the Hill</h1>
  <div class="subtitle">Trust, Service &amp; Devotion.</div>
  <div class="tagline">An Exquisite Women's Empowerment &amp; Prayer Brunch.</div>

  <div class="portrait speaker" role="img" aria-label="Portrait photo of guest speaker Minister Harriet L. Dunmore"></div>
  <p class="caption speaker">Guest Speaker<br>Minister Harriet L. Dunmore<br>Asst. Pastor &amp; First Lady of<br>Gilead Baptist Church<br>VP of TrustLine</p>

  <div class="portrait psalmist" role="img" aria-label="Portrait photo of special guest psalmist Minister Tessa Holbrook"></div>
  <p class="caption psalmist">Special Guest Psalmist<br>Minister Tessa Holbrook<br>Worship Director of<br>Stonefield Community Church<br>Vocalist, Songwriter,<br>Musician, and Clinician</p>

  <section class="venue">
    <div class="aboard">Aboard</div>
    <div class="yacht">Regal Tide Yacht</div>
    <div class="dock">Dock: Larkspur Landing</div>
    <div class="address">342 Marlow Court, Oxen Hill, MD 20712</div>
    <div class="boarding">Boarding 10:00am</div>
    <div class="sailing">Sailing Promptly at 10:30am</div>
    <div class="on-time">(Please be on time the yacht will not wait)</div>
  </section>

  <div class="date-pill">Saturday June 10, 2017</div>

  <p class="tickets">Early Bird US$75.00/person<br>(ends May 15, 2017)<br>Regular Tickets US$95.99</p>
  <p class="purchase">Purchase Tickets at<br>www.brightwellevent-travel.example/climbing-the-hill</p>
  <p class="capacity">SPACE IS LIMITED DUE TO YACHT CAPACITY</p>

  <svg class="prize-ribbon" viewBox="0 0 436 212" aria-hidden="true">
    <defs>
      <linearGradient id="boxFill" x1="0" y1="0" x2="0" y2="1">
        <stop offset="0" stop-color="#8a1c1c"/><stop offset="1" stop-color="#4e0f0f"/>
      </linearGradient>
      <linearGradient id="bandFill" x1="0" y1="0" x2="0" y2="1">
        <stop offset="0" stop-color="#fff3d6"/><stop offset="1" stop-color="#d9b872"/>
      </linearGradient>
    </defs>
    <path d="M6 22 L58 22 L58 98 L6 98 Z" fill="#c52222"/>
    <path d="M430 22 L378 22 L378 98 L430 98 Z" fill="#c52222"/>
    <path d="M24 34 Q218 -6 412 34 L412 102 Q218 62 24 102 Z" fill="url(#bandFill)" stroke="#b8902e" stroke-width="2"/>
    <path d="M44 52 Q218 14 392 52 L392 94 Q218 58 44 94 Z" fill="#b51f1f"/>
    <rect x="16" y="94" width="404" height="114" fill="url(#boxFill)" stroke="#c9a43a" stroke-width="3"/>
  </svg>
  <div class="prize-text">
    <div class="grand">Grand Prize : Julian Ardent Purse</div>
    <div class="door">Door Prize:&nbsp; 2 Tickets to the<br>Islander Coralwind Heritage Village</div>
    <div class="other">Other prizes for special ladies in attendance.</div>
  </div>

  <div class="dress-code">Ladies are asked to dress in Elegant White Ensemble</div>

  <div class="sponsor-bar">Sponsors</div>
  <div class="scene dance" role="img" aria-label="Photo of Coralwind Heritage Village dancers performing on stage"></div>
  <div class="sponsor-badge heritage">Coralwind Heritage Village</div>
  <div class="sponsor-badge lanning">R. Lanning Photography</div>
  <div class="scene fire" role="img" aria-label="Photo of a Coralwind Heritage Village fire dance performance at night"></div>

  <p class="thanks">Special Thanks to our Individual Sponsors:<br>Mrs. G. Whitlow, Mr. K Prentice &amp; Mr. S. Dorsey</p>
</main>
</body>
</html>
```